Infografiken für Rechtsfirma
Zielgruppe
Wir sind eine Rechtsfirma, welche sich mit dem europäischen Recht beschäftigt. Wir bieten Insolvenzen in unterschiedlichen Ländern an. Weiter beraten wir hinsichtlich des Vermögensschutzes. Wir helfen dabei, Vermögenswerte zu sichern. Für unseren Bereich Vermögensschutz benötigen wir eine Grafik, welche die Vorteile unseres Produkts direkt auf einen Blick erkennen lässt. Hierzu habe ich eine Grafik eines großen Mobilfunkherstellers beigefügt. Im gleichen Designe möchten wir diese Grafik haben.
Aufgabenstellung
Ich habe eine PDF-Datei (Vermögensschutz) beigefügt, aus welcher sich die Keyfacts ergeben. Diese müssen grafisch aufbereitet werden.

```html
<!DOCTYPE html>
<html lang="de">
<head>
<meta charset="utf-8">
<title>Vermögensschutz – Infografik</title>
<link rel="stylesheet" href="https://fonts.googleapis.com/css2?family=Fira+Sans+Condensed:wght@500;600;700&family=Fira+Sans:wght@400&display=swap">
<style>
  :root {
    --bg: #d1d2d4;
    --card: #ffffff;
    --purple: #7a4fa8;
    --deep-purple: #4a2e86;
    --brown: #c07a4a;
    --blue: #1f5fa8;
    --mid-blue: #2a6fb0;
    --sky: #38aed8;
    --red: #d6283a;
    --crimson: #e0185a;
    --orange: #f07a3a;
    --salmon: #f07a55;
    --gold: #c4a030;
    --amber: #f0900f;
    --green: #1a9a5a;
    --lime: #9ccc78;
    --teal-green: #5aa878;
    --label: #444444;
  }
  * { box-sizing: border-box; margin: 0; padding: 0; }
  html, body { width: 1200px; height: 784px; overflow: hidden; background: var(--bg); }
  body { position: relative; font-family: "Fira Sans Condensed", "Arial Narrow", sans-serif; font-weight: 700; }
  .card { position: absolute; background: var(--card); border-radius: 12px; }
  .abs { position: absolute; }
  .line { position: absolute; left: 0; right: 0; text-align: center; white-space: nowrap; line-height: 1; }
  .art { position: absolute; border-radius: 18px; }
  .label { position: absolute; width: 160px; margin-left: -80px; text-align: center; font-family: "Fira Sans", sans-serif; font-weight: 400; font-size: 16px; line-height: 1; color: var(--label); letter-spacing: .3px; }

  .anon { left: 20px; top: 20px; width: 278px; height: 286px; }
  .assets { left: 311px; top: 20px; width: 579px; height: 146px; }
  .exit-tax { left: 902px; top: 20px; width: 278px; height: 286px; }
  .transfer-tax { left: 20px; top: 319px; width: 278px; height: 287px; }
  .core { left: 311px; top: 178px; width: 579px; height: 428px; }
  .inherit { left: 902px; top: 319px; width: 278px; height: 287px; }
  .income { left: 20px; top: 619px; width: 278px; height: 145px; overflow: hidden; }
  .claims { left: 311px; top: 619px; width: 579px; height: 145px; }
  .insolvency { left: 902px; top: 619px; width: 278px; height: 145px; }

  .core-title { top: 14px; font-size: 35px; letter-spacing: 2px; }
  .legal-badge { position: absolute; left: 129px; top: 372px; width: 318px; height: 39px; border-radius: 14px; background: var(--lime); text-align: center; line-height: 39px; font-size: 22px; letter-spacing: 1px; }
  .shield-art { left: 174px; top: 67px; width: 232px; height: 288px; border-radius: 0;
    clip-path: polygon(8% 24%, 26% 4%, 50% 0, 74% 4%, 92% 24%, 90% 60%, 70% 86%, 50% 100%, 30% 86%, 10% 60%);
    background: radial-gradient(circle at 45% 40%, #e4e6e8, #9a9ea3 60%, #5e6268); }

  .secure-badge { position: absolute; left: 70px; top: 80px; width: 132px; height: 56px; border-radius: 28px; background: linear-gradient(#2c5bb0, #13367a); }
  .secure-badge::before { content: ""; position: absolute; left: 8px; top: 8px; width: 40px; height: 40px; border-radius: 50%; background: #3b8be0; border: 3px solid #0e2a62; }
</style>
</head>
<body>

<section class="card anon">
  <div class="line" style="top:4px;font-size:32px;color:var(--purple)">Anonymität</div>
  <div class="line" style="top:40px;font-size:27px;color:var(--brown)">Keine Rückschlüsse</div>
  <div class="line" style="top:72px;font-size:31px;color:var(--blue)">auf Sie möglich</div>
  <div class="abs" style="left:33px;top:112px;width:212px;height:4px;background:var(--red)"></div>
  <div class="art" role="img" aria-label="Sprechblase mit Personensymbol und durchgestrichene Figur als Null-Zeichen" style="left:46px;top:165px;width:198px;height:112px;border-radius:56px;background:linear-gradient(90deg,#cfe6f7,#e8f2fb 45%,#f2c2c4)"></div>
  <div class="abs" style="left:10px;top:160px;font-size:112px;line-height:1;color:var(--red)">1</div>
  <div class="abs" style="left:232px;top:160px;font-size:48px;line-height:1;color:var(--crimson)">%</div>
</section>

<section class="card assets">
  <div class="line" style="top:8px;font-size:29px">
    <span style="color:var(--orange)">Sicherung</span>
    <span style="color:var(--sky)">von</span>
    <span style="color:var(--green)">Vermögenswerten</span>
  </div>
  <div class="art" role="img" aria-label="Hand hält Haus – Immobilien" style="left:15px;top:38px;width:95px;height:82px;background:linear-gradient(#cfd8e2,#f3d3c6)"></div>
  <div class="art" role="img" aria-label="Hand mit Kryptomünzen" style="left:160px;top:38px;width:90px;height:82px;background:linear-gradient(#f6c24a,#f7d4c6)"></div>
  <div class="art" role="img" aria-label="Unterlagen mit Lupe, Rechner und Spielzeugauto" style="left:290px;top:40px;width:140px;height:80px;background:linear-gradient(#c8c9cb,#e6e6e6)"></div>
  <div class="art" role="img" aria-label="Urkunde mit Siegel – Firmenanteile" style="left:470px;top:42px;width:90px;height:78px;background:linear-gradient(135deg,#e27ad0,#b05ac8)"></div>
  <div class="label" style="left:69px;top:126px">Immobilien</div>
  <div class="label" style="left:208px;top:126px">Kryptowährung</div>
  <div class="label" style="left:362px;top:126px">Barvermögen</div>
  <div class="label" style="left:515px;top:126px">Firmenanteile</div>
</section>

<section class="card exit-tax">
  <div class="line" style="top:8px;font-size:29px;color:var(--crimson)">Wegzugsbesteuerung</div>
  <div class="line" style="top:41px;font-size:36px;color:var(--mid-blue)">Freiheit</div>
  <div class="art" role="img" aria-label="Hand hält rote Null mit Prozentzeichen" style="left:14px;top:90px;width:212px;height:180px;background:linear-gradient(120deg,#4f7fb8,#f2b9a6 45%,#e3214f)"></div>
</section>

<section class="card transfer-tax">
  <div class="line" style="top:14px;font-size:29px;color:var(--salmon)">Grunderwerbssteuer</div>
  <div class="line" style="top:47px;font-size:29px">
    <span style="color:var(--gold)">FREIE</span>
    <span style="color:var(--salmon)">Einbringung</span>
  </div>
  <div class="art" role="img" aria-label="Hand hält goldenes Null-Prozent-Zeichen" style="left:30px;top:100px;width:230px;height:165px;background:linear-gradient(120deg,#3a3d45,#f4b2a2 40%,#e8d048)"></div>
</section>

<section class="card core">
  <div class="line core-title">
    <span style="color:#6a4fa0">VERMÖGENS</span><span style="color:var(--mid-blue)">SCHUTZ</span>
  </div>
  <svg class="abs" style="left:0;top:0" width="579" height="428" viewBox="0 0 579 428" aria-hidden="true">
    <g fill="none" stroke-width="4" stroke-linecap="butt">
      <path d="M186 54 A190 190 0 0 0 107 157" stroke="#c3a8d9"/>
      <path d="M107 260 A190 190 0 0 0 189 364" stroke="#c3a8d9"/>
      <path d="M389 54 A190 190 0 0 1 471 157" stroke="#8fd3f2"/>
      <path d="M471 260 A190 190 0 0 1 390 364" stroke="#8fd3f2"/>
    </g>
    <g stroke="#6a4fa0" stroke-width="6" stroke-linecap="round" fill="none">
      <path d="M74 194 L95 217 L133 172"/>
      <path d="M100 226 L134 192"/>
      <path d="M108 236 L134 210"/>
      <path d="M116 245 L134 228"/>
    </g>
    <g fill="none" stroke="#2a6fb0" stroke-width="5">
      <path d="M448 179 L496 179 L496 239 L490 235 L483 240 L476 235 L469 240 L462 235 L455 240 L448 235 Z" stroke-linejoin="round"/>
      <line x1="461" y1="226" x2="484" y2="192"/>
    </g>
    <circle cx="462" cy="196" r="4.5" fill="#2a6fb0"/>
    <circle cx="482" cy="222" r="4.5" fill="#2a6fb0"/>
  </svg>
  <div class="art shield-art" role="img" aria-label="Schildförmiger Tresor mit Zahlenschloss und Griff"></div>
  <div class="legal-badge"><span style="color:#6a4fa0">LEGAL UND</span> <span style="color:var(--mid-blue)">RECHTSSICHER</span></div>
</section>

<section class="card inherit">
  <div class="line" style="top:14px;font-size:35px">
    <span style="color:var(--amber)">Erbschafts</span><span style="color:var(--purple)">steuer</span>
  </div>
  <div class="art" role="img" aria-label="Hand hält gelbe Null und violettes Prozentzeichen" style="left:18px;top:75px;width:240px;height:195px;background:linear-gradient(120deg,#f2c23a,#f6d2c2 45%,#8c6fd0)"></div>
</section>

<section class="card income">
  <div class="art" role="img" aria-label="Farbiges Tortendiagramm im Hintergrund" style="left:80px;top:0;width:150px;height:145px;border-radius:50%;background:conic-gradient(#f07ab8 0 25%,#7ab8ee 25% 55%,#f6c84a 55% 75%,#a68ad8 75% 100%);opacity:.85"></div>
  <div class="line" style="top:28px;font-size:25px;color:var(--deep-purple)">Steueroptimierung</div>
  <div class="line" style="top:57px;font-size:25px;color:var(--deep-purple)">für das laufende</div>
  <div class="line" style="top:86px;font-size:25px;color:var(--deep-purple)">Einkommen</div>
</section>

<section class="card claims">
  <div class="line" style="top:6px;font-size:30px">
    <span style="color:var(--sky)">Schutz</span>
    <span style="color:var(--blue)">vor</span>
    <span style="color:var(--orange)">Ansprüchen</span>
    <span style="color:var(--lime)">Dritter</span>
  </div>
  <div class="art" role="img" aria-label="Bankgebäude mit Geldscheinen und Karten" style="left:5px;top:54px;width:80px;height:66px;background:linear-gradient(#9a9ccc,#6fb37a)"></div>
  <div class="art" role="img" aria-label="Beleg mit Wecker und Münzen" style="left:105px;top:50px;width:78px;height:70px;background:linear-gradient(#c8d0f0,#f2b84a)"></div>
  <div class="art" role="img" aria-label="Schutzschild mit Schloss vor Geld" style="left:214px;top:52px;width:104px;height:68px;background:linear-gradient(120deg,#f2c23a,#a870d0 50%,#5ac070)"></div>
  <div class="art" role="img" aria-label="Klemmbrett mit Richterhammer" style="left:335px;top:48px;width:84px;height:72px;background:linear-gradient(#e6e4f2,#e8965a)"></div>
  <div class="art" role="img" aria-label="Hände halten ein rotes Herz" style="left:438px;top:56px;width:124px;height:62px;background:linear-gradient(90deg,#5a88c8,#d8283a 50%,#5a88c8)"></div>
  <div class="label" style="left:44px;top:125px">Bank</div>
  <div class="label" style="left:145px;top:125px">Finanzamt</div>
  <div class="label" style="left:270px;top:125px">Bürgschaften</div>
  <div class="label" style="left:388px;top:125px">Klage</div>
  <div class="label" style="left:500px;top:125px">Sozialversicherung</div>
</section>

<section class="card insolvency">
  <svg class="abs" style="left:20px;top:4px" width="56" height="68" viewBox="0 0 56 68" aria-hidden="true">
    <g stroke="var(--sky)" stroke-width="5" stroke-linecap="round" fill="none">
      <path d="M4 30 L20 46 L52 6"/>
      <path d="M24 54 L50 26"/>
      <path d="M31 60 L50 40"/>
      <path d="M38 65 L50 53"/>
    </g>
  </svg>
  <div class="abs" style="left:80px;top:3px;font-size:21px;line-height:22px;letter-spacing:.5px;white-space:nowrap">
    <div style="color:var(--lime)">Insolvenz sicher</div>
    <div style="color:var(--teal-green)">Kein Zugriff vom</div>
    <div style="color:var(--sky)">Insolvenzverwalter</div>
  </div>
  <div class="secure-badge" role="img" aria-label="Sicherheitssiegel"></div>
</section>

</body>
</html>
```